Trade Show Banner Stands

Looking for a fun, creative design to use for 2 banner stands - 85 X 200cm each, for an upcoming trade show in the biotech/pharma industry. We have a revolutionary product for use in the development of pharmaceutical drugs. Our equipment is unique and goals are to enhance our customers process development workflow, while maximizing their work space and generate more data with less operating and capital expenditures. Have included a file showing logo and color scheme and a couple photos for use. Website www.tovalix-bio.com. Interested in a innovative design that we can use and will amend wording once I start seeing designs. Thanks!

```html
<!DOCTYPE html>
<html lang="en">
<head>
<meta charset="utf-8">
<title>Tovalix Trade Show Banners</title>
<link href="https://fonts.googleapis.com/css2?family=Montserrat:wght@400;500;600;700;800;900&display=swap" rel="stylesheet">
<style>
  :root {
    --navy: #2f4a8b;
    --orange: #f06a0f;
    --white: #ffffff;
    --paper: #f4f5f7;
    --grey: #6f7178;
    --teal: #1fb3a6;
    --stage: #383838;
  }
  * { margin: 0; padding: 0; box-sizing: border-box; }
  html, body { width: 1200px; height: 1138px; overflow: hidden; }
  body {
    background: var(--stage);
    font-family: "Montserrat", sans-serif;
    position: relative;
  }
  .banner {
    position: absolute;
    top: 39px;
    width: 450px;
    height: 1060px;
    background: var(--paper);
    overflow: hidden;
  }
  .banner--left { left: 125px; }
  .banner--right { left: 625px; }
  .banner__shapes { position: absolute; inset: 0; }
  .headline {
    position: absolute;
    top: 34px; left: 0; width: 100%;
    text-align: center;
    color: var(--white);
    font-weight: 900;
    text-transform: uppercase;
    line-height: 1.02;
  }
  .headline span { display: block; }
  .headline__sm { font-size: 32px; letter-spacing: 1px; }
  .headline__lg { font-size: 48px; letter-spacing: 1px; }
  .benefit {
    position: absolute;
    color: var(--white);
    font-weight: 700;
    font-size: 17px;
    letter-spacing: .5px;
    text-transform: uppercase;
    line-height: 38px;
    height: 38px;
  }
  .benefit--workflows { top: 262px; left: 18px; }
  .benefit--workspace { top: 328px; left: 198px; }
  .benefit--throughput { top: 396px; left: 18px; }
  .info {
    position: absolute;
    top: 690px; left: 0; width: 100%;
    text-align: center;
    color: var(--navy);
  }
  .info__title { font-size: 30px; font-weight: 800; }
  .info__text { font-size: 14px; font-weight: 500; margin-top: 6px; line-height: 1.3; }
  .product-shot {
    position: absolute;
    top: 790px; left: 30px;
    width: 390px; height: 170px;
    background: linear-gradient(90deg, #d9dbe0 0%, #c3c6cd 45%, #e7e8eb 60%, #b84a63 80%, #e2e3e6 100%);
    border-radius: 6px;
  }
  .brand {
    position: absolute;
    top: 968px; left: 0; width: 100%;
    text-align: center;
  }
  .brand__name { font-size: 42px; font-weight: 700; color: var(--grey); line-height: 1; }
  .brand__company { font-size: 11px; font-weight: 700; color: var(--orange); margin-top: 4px; }
  .brand__url { font-size: 13px; font-weight: 500; color: var(--grey); margin-top: 2px; }
</style>
</head>
<body>

<section class="banner banner--left">
  <svg class="banner__shapes" viewBox="0 0 450 1060" width="450" height="1060" aria-hidden="true">
    <defs>
      <linearGradient id="photoTone" x1="0" y1="0" x2="1" y2="0.3">
        <stop offset="0" stop-color="#c9ccd6"/>
        <stop offset="0.45" stop-color="#8c93a8"/>
        <stop offset="0.7" stop-color="#2fb7aa"/>
        <stop offset="1" stop-color="#1a9e94"/>
      </linearGradient>
    </defs>
    <rect x="0" y="0" width="450" height="420" fill="var(--navy)"/>
    <path d="M0 650 L0 420 Q120 300 450 280 L450 560 Q300 660 0 650 Z" fill="url(#photoTone)" role="img" aria-label="Gloved hand holding a clear microfluidic chip"/>
    <path d="M0 650 Q300 660 450 560 L450 590 Q300 690 0 674 Z" fill="var(--orange)"/>
    <rect x="0" y="262" width="330" height="38" fill="var(--orange)"/>
    <circle cx="345" cy="266" r="32" fill="var(--orange)" stroke="var(--navy)" stroke-width="3"/>
    <circle cx="345" cy="266" r="13" fill="none" stroke="var(--white)" stroke-width="4" stroke-dasharray="5 3"/>
    <circle cx="345" cy="266" r="4" fill="var(--white)"/>
    <rect x="140" y="328" width="310" height="38" fill="var(--orange)"/>
    <circle cx="150" cy="334" r="32" fill="var(--orange)" stroke="var(--navy)" stroke-width="3"/>
    <g stroke="var(--white)" stroke-width="4" fill="none" stroke-linecap="round">
      <path d="M146 318 L156 340"/><path d="M136 352 L166 352"/><path d="M160 328 Q168 342 152 352"/>
    </g>
    <rect x="0" y="396" width="310" height="38" fill="var(--orange)"/>
    <circle cx="330" cy="400" r="32" fill="var(--orange)" stroke="var(--navy)" stroke-width="3"/>
    <g fill="var(--white)">
      <rect x="314" y="386" width="4" height="24"/><rect x="322" y="386" width="4" height="24"/>
      <rect x="330" y="386" width="4" height="24"/><rect x="338" y="386" width="4" height="24"/>
      <rect x="310" y="396" width="36" height="3"/><rect x="310" y="410" width="36" height="4"/>
    </g>
  </svg>
  <h1 class="headline">
    <span class="headline__sm">High Performance</span>
    <span class="headline__lg">Automated</span>
    <span class="headline__sm">True Perfusion</span>
    <span class="headline__sm">Microbioreactors</span>
  </h1>
  <p class="benefit benefit--workflows">Enhance Workflows</p>
  <p class="benefit benefit--workspace">Maximize Workspace</p>
  <p class="benefit benefit--throughput">Improve Throughput</p>
  <div class="info">
    <h2 class="info__title">What is Lorem Ipsum?</h2>
    <p class="info__text">Lorem Ipsum is simply dummy text of the printing<br>and typesetting industry.</p>
  </div>
  <div class="product-shot" role="img" aria-label="Bioreactor system with media bottles and laptop running control software"></div>
  <div class="brand">
    <p class="brand__name">tovalix</p>
    <p class="brand__company">Tovalix Biosystems, Inc</p>
    <p class="brand__url">www.tovalix-bio.com</p>
  </div>
</section>

<section class="banner banner--right">
  <svg class="banner__shapes" viewBox="0 0 450 1060" width="450" height="1060" aria-hidden="true">
    <defs>
      <linearGradient id="photoToneB" x1="0" y1="0" x2="1" y2="0.3">
        <stop offset="0" stop-color="#c9ccd6"/>
        <stop offset="0.45" stop-color="#8c93a8"/>
        <stop offset="0.7" stop-color="#2fb7aa"/>
        <stop offset="1" stop-color="#1a9e94"/>
      </linearGradient>
    </defs>
    <rect x="0" y="0" width="450" height="420" fill="var(--navy)"/>
    <path d="M0 650 L0 420 Q120 300 450 280 L450 560 Q300 660 0 650 Z" fill="url(#photoToneB)" role="img" aria-label="Gloved hand holding a clear microfluidic chip"/>
    <path d="M0 650 Q300 660 450 560 L450 590 Q300 690 0 674 Z" fill="var(--orange)"/>
    <rect x="0" y="262" width="330" height="38" fill="var(--orange)"/>
    <circle cx="345" cy="266" r="32" fill="var(--orange)" stroke="var(--navy)" stroke-width="3"/>
    <circle cx="345" cy="266" r="13" fill="none" stroke="var(--white)" stroke-width="4" stroke-dasharray="5 3"/>
    <circle cx="345" cy="266" r="4" fill="var(--white)"/>
    <rect x="140" y="328" width="310" height="38" fill="var(--orange)"/>
    <circle cx="150" cy="334" r="32" fill="var(--orange)" stroke="var(--navy)" stroke-width="3"/>
    <g stroke="var(--white)" stroke-width="4" fill="none" stroke-linecap="round">
      <path d="M146 318 L156 340"/><path d="M136 352 L166 352"/><path d="M160 328 Q168 342 152 352"/>
    </g>
    <rect x="0" y="396" width="310" height="38" fill="var(--orange)"/>
    <circle cx="330" cy="400" r="32" fill="var(--orange)" stroke="var(--navy)" stroke-width="3"/>
    <g fill="var(--white)">
      <rect x="314" y="386" width="4" height="24"/><rect x="322" y="386" width="4" height="24"/>
      <rect x="330" y="386" width="4" height="24"/><rect x="338" y="386" width="4" height="24"/>
      <rect x="310" y="396" width="36" height="3"/><rect x="310" y="410" width="36" height="4"/>
    </g>
  </svg>
  <h1 class="headline">
    <span class="headline__sm">High Performance</span>
    <span class="headline__lg">Automated</span>
    <span class="headline__sm">True Perfusion</span>
    <span class="headline__sm">Microbioreactors</span>
  </h1>
  <p class="benefit benefit--workflows">Enhance Workflows</p>
  <p class="benefit benefit--workspace">Maximize Workspace</p>
  <p class="benefit benefit--throughput">Improve Throughput</p>
  <div class="info">
    <h2 class="info__title">What is Lorem Ipsum?</h2>
    <p class="info__text">Lorem Ipsum is simply dummy text of the printing<br>and typesetting industry.</p>
  </div>
  <div class="product-shot" role="img" aria-label="Bioreactor system with media bottles and laptop running control software"></div>
  <div class="brand">
    <p class="brand__name">tovalix</p>
    <p class="brand__company">Tovalix Biosystems, Inc</p>
    <p class="brand__url">www.tovalix-bio.com</p>
  </div>
</section>

</body>
</html>
```